Redesign existing website

We would like a redesign of the website http://www.velbrisanalytics.com that creates a more modern, up to date look.

Velbris Analytics creates software for social science research and is focused on making the software user friendly and easy to use. We would like to convey seriousness, but also
a very up to date, just released look.

Feel free to modify the logo if you wish.

Target Market(s)

Academics, researchers

Industry/Entity Type

Software

Requirements
Must have
• The design should incorporate the same information as the current website.

```html
<!DOCTYPE html>
<html lang="en">
<head>
<meta charset="utf-8">
<title>Velbris Analytics</title>
<link href="https://fonts.googleapis.com/css2?family=Questrial&family=Arimo:ital,wght@0,400;0,700;1,400&display=swap" rel="stylesheet">
<style>
:root{
  --navy:#1f3a8f;
  --heading:#2d2f6b;
  --sky:#3aaee6;
  --sky-dark:#1b8fcc;
  --green:#7ed321;
  --green-dark:#4e9a10;
  --text:#444;
  --link:#1d9be0;
  --panel:#f2f2f2;
  --placeholder-top:#c9dcea;
  --placeholder-bottom:#e4ecf2;
}
*{box-sizing:border-box;margin:0;padding:0}
html,body{width:1049px;height:1200px;overflow:hidden;background:#fff}
body{font-family:"Arimo",Arial,sans-serif;color:var(--text)}
h2,h3{font-weight:400}
.page{position:relative;width:1000px;height:1144px;transform:scale(1.049);transform-origin:0 0;
  background:linear-gradient(180deg,#d6ecfa 0,#eef7fd 300px,#fff 470px,#fff 100%)}
.abs{position:absolute}

/* header */
.brand{left:30px;top:20px;width:176px;display:flex;flex-direction:column;align-items:center;gap:6px}
.brand-mark{width:72px;height:72px;border-radius:50%;background:var(--navy)}
.brand-name{font-family:"Questrial",sans-serif;font-size:22px;line-height:24px;color:var(--navy);white-space:nowrap}
.search{left:723px;top:98px;width:249px;height:28px;border:2px solid #6cc4ee;border-radius:3px;background:#fff;display:flex}
.search span{flex:1;font-size:13px;color:#333;padding:5px 0 0 18px}
.search-btn{width:36px;height:28px;margin:-2px -2px 0 0;background:var(--green);border-radius:0 3px 3px 0;display:flex;align-items:center;justify-content:center}

/* nav */
.nav-band{left:20px;top:147px;width:960px;height:51px;background:linear-gradient(180deg,#56b9ea,#2f9fd9);border-top:2px solid #1c88c6}
.content{left:20px;top:198px;width:960px;height:655px;background:#fff}
.nav-tab{top:160px;width:151px;height:38px;background:#fff;color:var(--navy);font-size:15px;text-align:center;padding-top:16px}
.nav-tab.active{top:150px;height:48px;padding-top:19px}

/* hero */
.hero-copy{left:34px;top:216px;width:301px;height:294px;background:linear-gradient(180deg,#4fb8ec,#2f9fd9);padding:72px 0 0 45px;
  font-family:"Questrial",sans-serif;font-size:27px;line-height:32px;color:#fff}
.hero-copy em{font-style:normal;color:var(--heading)}
.hero-slide{left:338px;top:216px;width:629px;height:294px;background:linear-gradient(180deg,var(--placeholder-top),var(--placeholder-bottom))}
.slide-caption{left:363px;top:483px;font-size:12px;color:#fff;text-shadow:0 0 3px rgba(0,0,0,.5)}
.dots{left:838px;top:478px;width:109px;height:24px;border-radius:6px;background:rgba(255,255,255,.4);display:flex;gap:9px;align-items:center;padding-left:9px}
.dots i{width:12px;height:12px;border-radius:50%;background:#fff}
.dots i.on{background:var(--sky-dark)}

/* sections */
.section-title{font-family:"Questrial",sans-serif;font-size:26px;line-height:30px;color:var(--heading);white-space:nowrap}
.icon-dot{width:28px;height:28px;border-radius:50%;background:linear-gradient(180deg,#eee,#999)}
.body-copy{font-size:12px;line-height:18px;color:var(--text)}
.divider-v{left:443px;top:565px;height:250px;border-left:1px dashed #ccc}
.sub-title{left:42px;top:729px;font-family:"Questrial",sans-serif;font-size:16px;color:var(--heading)}
.dl-btn{top:765px;width:180px;height:46px;border-radius:4px;background:linear-gradient(180deg,#555,#2f2f2f);color:#fff;padding:9px 0 0 12px;overflow:hidden}
.dl-btn b{display:block;font-size:15px;line-height:16px;white-space:nowrap}
.dl-btn small{display:block;font-size:11px;font-style:italic;color:#ccc;white-space:nowrap}
.dl-btn .ribbon{position:absolute;right:-12px;top:4px;width:44px;height:14px;background:var(--green);transform:rotate(45deg)}
.photo{top:596px;width:242px;height:127px;background:linear-gradient(135deg,#e8ddd2,#b59a84 55%,#5a4a44)}
.read-more{font-size:12px;color:var(--link)}
.divider-h{left:48px;top:851px;width:904px;border-top:2px dashed #ddd}

/* bottom boxes */
.box{top:905px;height:140px;border-radius:4px;border:2px solid #ccc;background:var(--panel)}
.box.blue{background:var(--sky);border-color:#5fc0ee}
.field{background:#fff;border:2px solid #ddd;border-radius:5px;height:27px}
.btn-green{background:var(--green);border:2px solid var(--green-dark);border-radius:3px;color:#222;font-size:12px;text-align:center;padding-top:5px;height:27px}
.label{font-size:12px;color:#222}
.box-title{font-size:21px;color:#222}

/* footer */
.footer-line{left:20px;top:1064px;width:960px;height:4px;background:#ddd}
.footer-links{left:0;top:1087px;width:1000px;text-align:center;font-size:12px;color:#333}
.copyright{left:0;top:1114px;width:1000px;text-align:center;font-size:12px;color:#333}
.connect{left:873px;top:1084px;font-size:12px;color:#333}
.social{top:1102px;width:28px;height:28px;border-radius:4px;background:linear-gradient(180deg,#e4edf6,#b8c9db)}
</style>
</head>
<body>
<div class="page">
  <header>
    <div class="abs brand"><span class="brand-mark"></span><span class="brand-name">Velbris Analytics</span></div>
    <div class="abs search"><span>Search</span>
      <div class="search-btn"><svg width="18" height="18" viewBox="0 0 18 18"><circle cx="7.5" cy="7.5" r="5" fill="none" stroke="#fff" stroke-width="2"/><line x1="11" y1="11" x2="16" y2="16" stroke="#fff" stroke-width="2.5"/></svg></div>
    </div>
  </header>

  <nav>
    <div class="abs nav-band"></div>
    <div class="abs nav-tab active" style="left:117px">Home</div>
    <div class="abs nav-tab" style="left:271px">Products</div>
    <div class="abs nav-tab" style="left:425px">News</div>
    <div class="abs nav-tab" style="left:579px">About us</div>
    <div class="abs nav-tab" style="left:733px">Contact us</div>
  </nav>
  <div class="abs content"></div>

  <section class="hero">
    <div class="abs hero-copy">Increasing the<br>power and<br>efficiency of<br>empirical <em>social<br>science research</em></div>
    <div class="abs hero-slide" role="img" aria-label="Slide photo: software window shown over an outdoor landscape"></div>
    <div class="abs slide-caption">Empowering the social science researcher</div>
    <div class="abs dots"><i class="on"></i><i></i><i></i><i></i><i></i></div>
  </section>

  <section class="welcome">
    <div class="abs icon-dot" style="left:47px;top:537px"></div>
    <h2 class="abs section-title" style="left:85px;top:537px">Welcome To Velbris Analytics</h2>
    <p class="abs body-copy" style="left:37px;top:588px;width:390px">The mission of Velbris Analytics, Inc. is to produce software products that multiply the power and efficiency of empirical scientific research in the social sciences.</p>
    <p class="abs body-copy" style="left:37px;top:660px;width:390px">A central goal is to expand access to complex data sources and to the advanced methods of scientific investigation needed to analyze them.</p>
    <h3 class="abs sub-title">Velbris Data Manager</h3>
    <div class="abs dl-btn" style="left:36px"><b>Velbris Data Manager</b><small>Preview Release Available!</small><span class="ribbon"></span></div>
    <div class="abs dl-btn" style="left:229px"><b>Velbris Data Manager</b><small>Download Preview Release</small><span class="ribbon"></span></div>
  </section>
  <div class="abs divider-v"></div>

  <section class="solution">
    <div class="abs icon-dot" style="left:472px;top:533px;border-radius:50% 50% 30% 30%"></div>
    <h2 class="abs section-title" style="left:510px;top:537px">Latest Solution</h2>
    <div class="abs photo" style="left:470px" role="img" aria-label="Photo: colleagues talking in a meeting"></div>
    <div class="abs photo" style="left:731px" role="img" aria-label="Photo: business team working at laptops"></div>
    <p class="abs body-copy" style="left:473px;top:733px;width:245px">These cases are perfectly simple and easy to distinguish. In a free hour, when our power of choice is untrammelled and when nothing prevents.</p>
    <p class="abs body-copy" style="left:733px;top:733px;width:245px">These cases are perfectly simple and easy to distinguish. In a free hour, when our power of choice is untrammelled and when nothing prevents.</p>
    <a class="abs read-more" style="left:472px;top:813px">» Read more</a>
    <a class="abs read-more" style="left:732px;top:813px">» Read more</a>
  </section>
  <div class="abs divider-h"></div>

  <section class="newsletter">
    <div class="abs icon-dot" style="left:30px;top:868px;border-radius:4px"></div>
    <h2 class="abs section-title box-title" style="left:75px;top:870px">News letter</h2>
    <div class="abs box blue" style="left:20px;width:273px"></div>
    <div class="abs label" style="left:42px;top:937px;color:#fff">Enter your E-mail</div>
    <div class="abs field" style="left:34px;top:957px;width:248px"></div>
    <div class="abs btn-green" style="left:115px;top:1007px;width:88px">Subscribe</div>
  </section>

  <section class="news">
    <div class="abs icon-dot" style="left:320px;top:868px;border-radius:3px"></div>
    <h2 class="abs section-title box-title" style="left:363px;top:870px">Latest News</h2>
    <div class="abs label" style="left:567px;top:877px;color:#777">‹ ›</div>
    <div class="abs box" style="left:311px;width:283px"></div>
    <div class="abs label" style="left:345px;top:925px;font-weight:700">Nov 12 2011</div>
    <div class="abs label" style="left:508px;top:925px">2.50 pm</div>
    <p class="abs body-copy" style="left:342px;top:956px;width:230px">The wise man therefore always holds in these matters to this principle of selection: he rejects pleasures to secure..</p>
    <a class="abs read-more" style="left:502px;top:1020px">» Read more</a>
  </section>

  <section class="login">
    <div class="abs icon-dot" style="left:631px;top:870px"></div>
    <h2 class="abs section-title box-title" style="left:668px;top:870px">Log in</h2>
    <div class="abs box" style="left:612px;width:368px"></div>
    <div class="abs label" style="left:638px;top:930px">User Name</div>
    <div class="abs field" style="left:703px;top:924px;width:239px"></div>
    <div class="abs label" style="left:638px;top:975px">Password</div>
    <div class="abs field" style="left:703px;top:968px;width:239px"></div>
    <svg class="abs" style="left:648px;top:1010px" width="13" height="13" viewBox="0 0 13 13"><rect x=".5" y=".5" width="12" height="12" fill="#fff" stroke="#666"/><path d="M3 6.5l2.5 2.5L10 3.5" fill="none" stroke="#1f3a8f" stroke-width="1.6"/></svg>
    <div class="abs label" style="left:668px;top:1009px">Forgot password?</div>
    <div class="abs btn-green" style="left:857px;top:1007px;width:88px">Subscribe</div>
  </section>

  <footer>
    <div class="abs footer-line"></div>
    <div class="abs footer-links">Home | Products | News | About us | Contact us</div>
    <div class="abs copyright">All © Copyrights .velbris analytics</div>
    <div class="abs connect">Connect with us:</div>
    <div class="abs social" style="left:866px"></div>
    <div class="abs social" style="left:901px"></div>
    <div class="abs social" style="left:936px;background:linear-gradient(180deg,#fbd3a8,#f08a2c)"></div>
  </footer>
</div>
</body>
</html>
```